A clean crisp business card for a Landscape Construction company. Designed to be easy to read contact/ info and also be appealing/interesting, unlike a traditional business card.

Industry/Entity Type

Landscape Construction

Contact Information for Business Card

Company name : Bramblecrest Landscape Construction, phone number: (877) 62Vales, website:Bramblecrestlandscapes.example, Email, sales@bramblecrestlandscapes.example

Requirements
Nice to have
• Luxurious finishes/ details…. Icons or emblems next to contact info
Should not have
• Clipart or general pictures

```html
<!DOCTYPE html>
<html lang="en">
<head>
<meta charset="UTF-8">
<title>Bramblecrest Landscape Construction – Business Card</title>
<link rel="stylesheet" href="https://fonts.googleapis.com/css2?family=Montserrat:wght@400;600;700&display=swap">
<style>
  :root {
    --backdrop: #2a2a2a;
    --card-black: #050505;
    --card-white: #ffffff;
    --leaf-green: #9ccc3c;
    --leaf-green-glow: rgba(156, 204, 60, 0.75);
    --leaf-green-fade: rgba(156, 204, 60, 0);
    --water-blue: #1f6cc4;
    --ink: #222222;
    --ink-soft: #444444;
  }
  * { margin: 0; padding: 0; box-sizing: border-box; }
  html, body {
    width: 1200px; height: 900px; overflow: hidden;
    background: var(--backdrop);
    font-family: "Montserrat", sans-serif;
  }
  .canvas {
    position: relative; width: 1200px; height: 900px;
    display: flex; flex-direction: column; align-items: center; justify-content: center; gap: 34px;
  }
  .card {
    position: relative; width: 640px; height: 366px; overflow: hidden;
    box-shadow: 0 14px 30px rgba(0,0,0,0.55);
  }
  .card--back {
    background: var(--card-black);
    display: flex; align-items: center; justify-content: center;
  }
  .card--front { background: var(--card-white); }

  .wordmark { display: flex; align-items: center; gap: 14px; }
  .wordmark__dot {
    width: 30px; height: 30px; border-radius: 50%; background: var(--water-blue); flex: none;
  }
  .wordmark__name {
    font-weight: 600; color: var(--leaf-green); line-height: 1.15; letter-spacing: 0.04em;
  }
  .card--back .wordmark__name { font-size: 30px; }
  .wordmark__name span { display: block; font-size: 0.5em; letter-spacing: 0.22em; text-transform: uppercase; }

  .swoosh { position: absolute; left: 0; top: 0; width: 640px; height: 366px; }
  .corner-foliage {
    position: absolute; right: 0; top: 0; width: 170px; height: 150px;
    background: radial-gradient(ellipse at 100% 0%, var(--leaf-green-glow) 0%, var(--leaf-green-fade) 70%);
  }

  .front-brand { position: absolute; left: 36px; top: 212px; }
  .front-brand .wordmark__name { font-size: 24px; }
  .front-brand .wordmark__dot { width: 24px; height: 24px; }

  .divider {
    position: absolute; left: 338px; top: 150px; width: 3px; height: 170px; background: var(--water-blue);
  }
  .contact { position: absolute; left: 364px; top: 140px; width: 260px; }
  .contact__name { font-size: 25px; font-weight: 700; color: var(--leaf-green); line-height: 1.1; }
  .contact__role { font-size: 14px; color: var(--ink-soft); letter-spacing: 0.05em; margin: 2px 0 16px 10px; }
  .contact__list { list-style: none; }
  .contact__item {
    display: flex; align-items: flex-start; gap: 10px;
    font-size: 11px; color: var(--ink); line-height: 1.4; margin-bottom: 5px;
  }
  .contact__item--address { margin-bottom: 14px; }
  .contact__icon { width: 14px; height: 14px; flex: none; margin-top: 1px; }
</style>
</head>
<body>
<main class="canvas">

  <section class="card card--back" aria-label="Card back">
    <div class="wordmark">
      <div class="wordmark__dot"></div>
      <p class="wordmark__name">Bramblecrest<span>Landscape Construction</span></p>
    </div>
  </section>

  <section class="card card--front" aria-label="Card front">
    <svg class="swoosh" viewBox="0 0 640 366" aria-hidden="true">
      <path d="M0,0 L640,0 L640,8 C430,26 210,66 0,74 Z" fill="var(--leaf-green)"/>
      <path d="M0,94 C170,92 300,62 420,24 C310,70 170,106 0,116 Z" fill="var(--water-blue)"/>
    </svg>
    <div class="corner-foliage" role="img" aria-label="Green vine and leaf ornament in the top corner"></div>

    <div class="front-brand">
      <div class="wordmark">
        <div class="wordmark__dot"></div>
        <p class="wordmark__name">Bramblecrest<span>Landscape Construction</span></p>
      </div>
    </div>

    <div class="divider"></div>

    <div class="contact">
      <h1 class="contact__name">Owen Haverly</h1>
      <p class="contact__role">CEO</p>
      <ul class="contact__list">
        <li class="contact__item contact__item--address">
          <svg class="contact__icon" viewBox="0 0 14 14"><path d="M7 1a4 4 0 0 1 4 4c0 3-4 8-4 8S3 8 3 5a4 4 0 0 1 4-4z" fill="var(--leaf-green)"/><circle cx="7" cy="5" r="1.5" fill="#fff"/></svg>
          <span>4120 Larkspur Meadow Rd.,<br>Suite 12, Fairbrook, OH 45000</span>
        </li>
        <li class="contact__item">
          <svg class="contact__icon" viewBox="0 0 14 14"><circle cx="7" cy="7" r="6" fill="none" stroke="var(--leaf-green)" stroke-width="1.5"/><path d="M5 4.5l1 1.5-.7.8a4 4 0 0 0 1.9 1.9l.8-.7 1.5 1-.6 1.1C6.5 10 4 7.5 3.9 5.1z" fill="var(--leaf-green)"/></svg>
          <span>(877) 62Vales</span>
        </li>
        <li class="contact__item">
          <svg class="contact__icon" viewBox="0 0 14 14"><rect x="1" y="3" width="12" height="8" fill="var(--leaf-green)"/><path d="M1 3l6 5 6-5" fill="none" stroke="#fff" stroke-width="1"/></svg>
          <span>sales@bramblecrestlandscapes.example</span>
        </li>
        <li class="contact__item">
          <svg class="contact__icon" viewBox="0 0 14 14"><circle cx="7" cy="7" r="6" fill="var(--leaf-green)"/><path d="M1 7h12M7 1c2.5 3 2.5 9 0 12M7 1c-2.5 3-2.5 9 0 12" fill="none" stroke="#fff" stroke-width="0.8"/></svg>
          <span>www.bramblecrestlandscapes.example</span>
        </li>
      </ul>
    </div>
  </section>

</main>
</body>
</html>
```